A banner for a fully digital bank.

In need of banners for the “Q7 Bank”. Has to show us not as just another digital bank, but a bank in whom ordinary people can trust. We won’t charge overdraft fees, transaction fees etc as a normal stationary bank would. We also will work with crypto, and be as user friendly as possible.

Banking

```html
<!DOCTYPE html>
<html lang="en">
<head>
<meta charset="utf-8">
<title>Q7 Bank – Digital Banking Banner</title>
<link rel="stylesheet" href="https://fonts.googleapis.com/css2?family=Montserrat:wght@500;700&family=Nunito:wght@700;800&display=swap">
<style>
  :root {
    --page-bg: #2b2b2e;
    --banner-deep: #1c0a58;
    --banner-mid: #2c0862;
    --banner-violet: #45096e;
    --banner-edge: #4a1590;
    --accent-cyan: #35e2f2;
    --text-white: #ffffff;
    --art-lilac: #b69ae6;
    --art-lilac-soft: #8e6fd6;
    --art-indigo: #3a2696;
    --art-gold: #f4b63f;
    --art-blue: #4f8ff0;
    --glow-pink: rgba(206, 70, 255, 0.40);
  }
  * { box-sizing: border-box; margin: 0; padding: 0; }
  html, body {
    width: 1200px;
    height: 840px;
    overflow: hidden;
    background: var(--page-bg);
  }
  .banner {
    position: absolute;
    left: 0;
    top: 120px;
    width: 1200px;
    height: 600px;
    overflow: hidden;
    background:
      radial-gradient(ellipse 45% 60% at 78% 55%, rgba(120, 20, 160, 0.55), transparent 70%),
      linear-gradient(100deg, var(--banner-deep) 0%, var(--banner-mid) 40%, var(--banner-violet) 75%, var(--banner-edge) 100%);
    font-family: "Montserrat", sans-serif;
    color: var(--text-white);
  }
  .brand-name {
    position: absolute;
    left: 90px;
    top: 76px;
    font-family: "Montserrat", sans-serif;
    font-weight: 700;
    font-size: 54px;
    letter-spacing: 0;
    line-height: 1;
  }
  .tagline {
    position: absolute;
    left: 90px;
    top: 172px;
    height: 148px;
    padding-left: 20px;
    border-left: 2px solid var(--text-white);
    font-family: "Nunito", sans-serif;
    font-weight: 800;
    font-size: 31px;
    line-height: 35.5px;
  }
  .tagline .tagline-accent { color: var(--accent-cyan); display: block; }
  .tagline .tagline-main { color: var(--text-white); display: block; }
  .features {
    position: absolute;
    left: 90px;
    top: 355px;
    list-style: none;
  }
  .feature {
    display: flex;
    align-items: center;
    height: 46px;
    margin-bottom: 15px;
  }
  .feature-icon { width: 46px; height: 46px; flex: none; }
  .feature-text {
    margin-left: 16px;
    font-weight: 500;
    font-size: 14.5px;
    line-height: 18px;
  }
  .illustration-glow {
    position: absolute;
    left: 560px;
    top: 80px;
    width: 540px;
    height: 480px;
    border-radius: 50%;
    background: radial-gradient(circle at 50% 50%, var(--glow-pink), transparent 65%);
  }
  .illustration {
    position: absolute;
    left: 492px;
    top: 27px;
    width: 652px;
    height: 554px;
    clip-path: polygon(38% 0%, 62% 8%, 86% 26%, 100% 48%, 100% 86%, 55% 100%, 0% 82%, 0% 32%);
    background:
      radial-gradient(circle at 46% 14%, var(--art-gold) 0%, rgba(244, 182, 63, 0) 16%),
      radial-gradient(ellipse at 50% 52%, var(--art-lilac) 0%, rgba(182, 154, 230, 0) 38%),
      radial-gradient(ellipse at 20% 70%, rgba(79, 143, 240, 0.55) 0%, rgba(79, 143, 240, 0) 28%),
      linear-gradient(160deg, var(--art-lilac-soft) 0%, var(--art-indigo) 70%, rgba(58, 38, 150, 0.6) 100%);
    opacity: 0.85;
  }
</style>
</head>
<body>
  <section class="banner">
    <h1 class="brand-name">Q7 BANK</h1>

    <p class="tagline">
      <span class="tagline-accent">Not&nbsp; just another<br>digital bank,</span>
      <span class="tagline-main">but a bank in which<br>you can trust</span>
    </p>

    <ul class="features">
      <li class="feature">
        <svg class="feature-icon" viewBox="0 0 46 46" aria-hidden="true">
          <circle cx="23" cy="23" r="21.5" fill="none" stroke="var(--accent-cyan)" stroke-width="1.5"/>
          <circle cx="23" cy="23" r="12" fill="none" stroke="#fff" stroke-width="1.6"/>
          <circle cx="23" cy="23" r="8" fill="none" stroke="#fff" stroke-width="1.2"/>
          <line x1="14" y1="32" x2="32" y2="14" stroke="#fff" stroke-width="1.8"/>
        </svg>
        <span class="feature-text">No overdraft fees or<br>transaction fees</span>
      </li>
      <li class="feature">
        <svg class="feature-icon" viewBox="0 0 46 46" aria-hidden="true">
          <circle cx="23" cy="23" r="21.5" fill="none" stroke="var(--accent-cyan)" stroke-width="1.5"/>
          <circle cx="19" cy="26" r="8" fill="none" stroke="#fff" stroke-width="1.6"/>
          <circle cx="28" cy="19" r="7" fill="none" stroke="#fff" stroke-width="1.6"/>
          <path d="M17 22v8M17 22h3a2 2 0 0 1 0 4h-3M17 26h3.5a2 2 0 0 1 0 4H17" fill="none" stroke="#fff" stroke-width="1.3"/>
          <path d="M30 16h-3a1.5 1.5 0 0 0 0 3h2a1.5 1.5 0 0 1 0 3h-3M28 14.5v9" fill="none" stroke="#fff" stroke-width="1.3"/>
        </svg>
        <span class="feature-text">We also work<br>with crypto</span>
      </li>
      <li class="feature">
        <svg class="feature-icon" viewBox="0 0 46 46" aria-hidden="true">
          <circle cx="23" cy="23" r="21.5" fill="none" stroke="var(--accent-cyan)" stroke-width="1.5"/>
          <rect x="15" y="13" width="18" height="13" rx="1.5" fill="none" stroke="#fff" stroke-width="1.6"/>
          <rect x="11" y="20" width="7" height="13" rx="1.2" fill="var(--banner-mid)" stroke="#fff" stroke-width="1.5"/>
          <rect x="28" y="23" width="6" height="10" rx="1" fill="var(--banner-mid)" stroke="#fff" stroke-width="1.4"/>
          <line x1="19" y1="30" x2="27" y2="30" stroke="#fff" stroke-width="1.6"/>
        </svg>
        <span class="feature-text">An user friendly bank<br>that you always wanted</span>
      </li>
    </ul>

    <div class="illustration-glow" aria-hidden="true"></div>
    <div class="illustration" role="img" aria-label="Isometric illustration of a bank building with a gold coin dropping into its roof, surrounded by a wallet with coins, a smartphone shopping screen, a piggy bank, an ATM, a credit card with a receipt and a card payment terminal, linked by glowing circuit lines"></div>
  </section>
</body>
</html>
```